Dale Merrow Broker owner of Real Estate Company

Dale Merrow, GRI CRS ABR
Broker Owner
586-317-4902
dalemerrow@dalemerrowrealtors.example
14637 Larkspur Ave. Lakeview Harbor, MI 48207
Licensed in Ohio and South Carolina
"35 Years of Dependable Service built on a Results Focused Selling Plan"

```html
<!DOCTYPE html>
<html lang="en">
<head>
<meta charset="utf-8">
<title>Dale Merrow – Business Card</title>
<link href="https://fonts.googleapis.com/css2?family=Montserrat:wght@400;500;800&display=swap" rel="stylesheet">
<style>
  :root {
    --backdrop: #6e3d20;
    --card: #1a1a1a;
    --text: #f2f2f2;
    --gold: #e9b45c;
  }
  * { margin: 0; padding: 0; box-sizing: border-box; }
  html, body { width: 1200px; height: 848px; overflow: hidden; }
  body {
    background: var(--backdrop);
    font-family: "Montserrat", sans-serif;
    position: relative;
  }
  .card {
    position: absolute;
    top: 127px;
    width: 335px;
    height: 586px;
    background: var(--card);
    color: var(--text);
    box-shadow: 0 6px 18px rgba(0,0,0,0.35);
    text-align: center;
  }
  .card--back { left: 242px; }
  .card--front { left: 612px; }

  .icon { display: block; margin: 0 auto; }
  .contact { position: absolute; left: 0; right: 0; top: 336px; }
  .address { margin-top: 6px; font-size: 13.5px; line-height: 19px; }
  .icon-row { display: flex; justify-content: center; gap: 4px; margin-top: 17px; }
  .details { margin-top: 8px; font-size: 13.5px; line-height: 19px; }
  .tagline { margin-top: 15px; font-size: 13.5px; line-height: 19px; }

  .portrait {
    position: absolute; left: 0; top: 0; width: 100%; height: 478px;
    background: linear-gradient(180deg, #3b4640 0%, #6f7670 35%, #4a4f57 62%, #2f3540 100%);
  }
  .identity { position: absolute; left: 0; right: 0; top: 490px; }
  .name { font-weight: 800; font-size: 20.5px; color: var(--gold); letter-spacing: 0.2px; }
  .role { font-size: 13.5px; margin-top: 2px; }
  .license { font-size: 13.5px; color: var(--gold); margin-top: 11px; }
</style>
</head>
<body>
  <section class="card card--back">
    <div class="contact">
      <svg class="icon" width="22" height="22" viewBox="0 0 22 22" aria-hidden="true">
        <circle cx="11" cy="11" r="10" fill="none" stroke="var(--gold)" stroke-width="1.3"/>
        <path d="M11 5.2a3.8 3.8 0 0 0-3.8 3.8c0 2.8 3.8 7 3.8 7s3.8-4.2 3.8-7A3.8 3.8 0 0 0 11 5.2z" fill="var(--gold)"/>
        <circle cx="11" cy="9" r="1.4" fill="var(--card)"/>
      </svg>
      <p class="address">14637 Larkspur Ave.<br>Lakeview Harbor, MI 48207</p>
      <div class="icon-row" aria-hidden="true">
        <svg width="21" height="21" viewBox="0 0 22 22">
          <circle cx="11" cy="11" r="10" fill="none" stroke="var(--gold)" stroke-width="1.3"/>
          <path d="M7.5 6c.6-.4 1.2-.3 1.5.2l1 1.6c.3.5.1 1-.3 1.3l-.6.5c.6 1.3 1.6 2.3 2.9 2.9l.5-.6c.3-.4.9-.6 1.3-.3l1.6 1c.5.3.6.9.2 1.5-.6.9-1.6 1.3-2.6.9-2.8-1-4.8-3-5.8-5.8-.4-1 0-2 .3-2.2z" fill="none" stroke="var(--gold)" stroke-width="1.1"/>
        </svg>
        <svg width="21" height="21" viewBox="0 0 22 22">
          <circle cx="11" cy="11" r="10" fill="none" stroke="var(--gold)" stroke-width="1.3"/>
          <rect x="6" y="7.5" width="10" height="7" fill="var(--gold)"/>
          <path d="M6 7.5l5 4 5-4" fill="none" stroke="var(--card)" stroke-width="1"/>
        </svg>
        <svg width="21" height="21" viewBox="0 0 22 22">
          <circle cx="11" cy="11" r="10" fill="none" stroke="var(--gold)" stroke-width="1.3"/>
          <g fill="none" stroke="var(--gold)" stroke-width="0.9">
            <circle cx="11" cy="11" r="5.2"/>
            <ellipse cx="11" cy="11" rx="2.2" ry="5.2"/>
            <path d="M5.8 11h10.4M6.6 8.4h8.8M6.6 13.6h8.8"/>
          </g>
        </svg>
      </div>
      <p class="details">586-317-4902<br>dalemerrow@dalemerrowrealtors.example<br>www.dalemerrowrealtors.example</p>
      <p class="tagline">35 Years of Dependable Service built<br>on a Results Focused Selling Plan</p>
    </div>
  </section>

  <section class="card card--front">
    <div class="portrait" role="img" aria-label="Studio portrait of Dale Merrow in a grey suit and patterned tie against a cloudy backdrop"></div>
    <div class="identity">
      <h1 class="name">Dale Merrow, GRI CRS ABR</h1>
      <p class="role">Broker Owner</p>
      <p class="license">Licensed in Ohio and South Carolina</p>
    </div>
  </section>
</body>
</html>
```